Harbourline Property Care Heating Services, needs a business card Design

We need a business card design for a company in the United Kingdom, we work mainly in London in Domestic Plumbing & Heating and would like to branch out (more) in to the Commercial aspect of the business.
We need the card to promote care, trust, professionalism, because we do, if possible, we will always better or match prices with an over all better experience for clients.

Info to add on card...

My name... Declan Hursey
Cell... 07491186752
Email... declanhursey00@Mailvex.com
Business/Post code... KT7 4WX

Thanks

Declan

Hi there updated my design project! If you could please look through again and add as much as possable (as you will see) I'd be very grateful! Although I do enjoy seeing all your fantastic designs, I don't want to spend the remaining 14 days being hard to please. PS.. I'm from NZ but living in UK, if you find patriotic (NZ) that is do add in. Not of huge importance but It dose get peoples attention! Thanks a lot, Declan

I work in Chelsea and most of my days so think Chelsea.

Thanks.

Business

Serif
Sans Serif

• Just want text to be as easy to read as possible!

Would like to see some or all pictures I have on the card if at all possible.
They are well known logos in my industry.
And my team and I are all fully qualified in these different schemes.

Also a break down of services I provide!

- Central Heating Engineering.
- Bathroom and Kitchen Fitting.
- Plumbing.
- Electrical.
- Tiling.
- All Your Carpentry and Building Needs.

Thanks.

• Only restriction no pink otherwise go for it!

Thanks.

```html
<!DOCTYPE html>
<html lang="en">
<head>
<meta charset="utf-8">
<title>Harbourline Property Care – Business Card</title>
<link rel="stylesheet" href="https://fonts.googleapis.com/css2?family=Exo+2:wght@400;500&display=swap">
<style>
  :root {
    --stage: #e4e6ec;
    --card-white: #f4f5f6;
    --blue-light: #1c9ddb;
    --blue-deep: #0d6db3;
    --green: #6cbf4a;
    --brand-blue: #1f7cc3;
    --ink-light: #ffffff;
  }
  * { box-sizing: border-box; margin: 0; padding: 0; }
  html, body {
    width: 1200px; height: 840px; overflow: hidden;
    background: var(--stage);
  }
  .card {
    position: absolute; left: 100px; top: 134px;
    width: 1000px; height: 572px;
    background: var(--card-white);
    box-shadow: 0 12px 36px rgba(30, 40, 60, 0.18);
    overflow: hidden;
    font-family: "Exo 2", "Segoe UI", sans-serif;
  }
  .card__shapes { position: absolute; inset: 0; }
  .holder {
    position: absolute; left: 48px; top: 120px;
    color: var(--ink-light);
  }
  .holder__name { font-size: 31px; font-weight: 500; letter-spacing: 2px; text-transform: uppercase; }
  .holder__role { font-size: 18px; letter-spacing: 1.5px; text-transform: uppercase; margin-top: 4px; }
  .address {
    position: absolute; left: 48px; top: 248px;
    color: var(--ink-light); font-size: 20px; line-height: 30px; letter-spacing: 1px;
  }
  .contacts {
    position: absolute; left: 48px; top: 360px;
    list-style: none; color: var(--ink-light); font-size: 18px; letter-spacing: 1px;
  }
  .contacts li { display: flex; align-items: center; height: 34px; }
  .contacts svg { width: 18px; height: 18px; margin-right: 12px; fill: var(--ink-light); }
  .brand {
    position: absolute; left: 580px; top: 70px; width: 360px;
    text-align: center; color: var(--brand-blue);
  }
  .brand__dot {
    width: 64px; height: 64px; border-radius: 50%;
    background: var(--brand-blue); margin: 0 auto 26px;
  }
  .brand__name { font-size: 25px; font-weight: 500; line-height: 30px; letter-spacing: 1px; }
</style>
</head>
<body>
  <div class="card">
    <svg class="card__shapes" viewBox="0 0 1000 572" aria-hidden="true">
      <defs>
        <radialGradient id="blueField" cx="35%" cy="50%" r="65%">
          <stop offset="0" stop-color="var(--blue-light)"/>
          <stop offset="1" stop-color="var(--blue-deep)"/>
        </radialGradient>
      </defs>
      <path class="wave-accent" fill="var(--green)"
        d="M0,0 L380,0 C470,40 420,210 505,300 C580,385 590,470 555,545 L0,545 Z"/>
      <path class="wave-field" fill="url(#blueField)"
        d="M0,0 L330,0 C430,40 390,205 475,300 C545,380 565,470 530,545 L1000,545 L1000,572 L0,572 Z"/>
      <rect class="base-band" x="0" y="540" width="1000" height="32" fill="var(--blue-deep)"/>
    </svg>

    <div class="holder">
      <p class="holder__name">Declan Hursey</p>
      <p class="holder__role">Financial Advisor</p>
    </div>

    <p class="address">042.2nd floor,Park Lane<br>Road KT7 4WX</p>

    <ul class="contacts">
      <li><svg viewBox="0 0 24 24"><path d="M6.6 10.8a15 15 0 0 0 6.6 6.6l2.2-2.2a1 1 0 0 1 1-.25 11 11 0 0 0 3.6.6 1 1 0 0 1 1 1V20a1 1 0 0 1-1 1A17 17 0 0 1 3 4a1 1 0 0 1 1-1h3.5a1 1 0 0 1 1 1 11 11 0 0 0 .6 3.6 1 1 0 0 1-.25 1z"/></svg>07491186752</li>
      <li><svg viewBox="0 0 24 24"><path d="M7 1h10a2 2 0 0 1 2 2v18a2 2 0 0 1-2 2H7a2 2 0 0 1-2-2V3a2 2 0 0 1 2-2zm0 3v15h10V4zm5 16.2a1 1 0 1 0 0 .01z"/></svg>07491186752</li>
      <li><svg viewBox="0 0 24 24"><path d="M6 2h9v5H6zM3 8h18v12H3zm3 3v2h3v-2zm5 0v2h3v-2zm5 0v2h2v-2zM6 15v2h3v-2zm5 0v2h3v-2z"/></svg>07491186752</li>
      <li><svg viewBox="0 0 24 24"><path d="M2 5h20v14H2zm2 2v.5l8 5.5 8-5.5V7zm0 3v7h16v-7l-8 5.5z"/></svg>declanhursey00@Mailvex.com</li>
      <li><svg viewBox="0 0 24 24"><path d="M12 2a10 10 0 1 0 0 20 10 10 0 0 0 0-20zm6.9 9h-3a15 15 0 0 0-1.4-6 8 8 0 0 1 4.4 6zM12 4.1c.9 1.3 1.8 3.6 1.9 6.9h-3.8c.1-3.3 1-5.6 1.9-6.9zM9.5 5a15 15 0 0 0-1.4 6h-3a8 8 0 0 1 4.4-6zm-4.4 8h3a15 15 0 0 0 1.4 6 8 8 0 0 1-4.4-6zm6.9 6.9c-.9-1.3-1.8-3.6-1.9-6.9h3.8c-.1 3.3-1 5.6-1.9 6.9zm2.5-.9a15 15 0 0 0 1.4-6h3a8 8 0 0 1-4.4 6z"/></svg>www.harbourlinecare.co.uk</li>
    </ul>

    <div class="brand">
      <div class="brand__dot"></div>
      <p class="brand__name">Harbourline Property Care<br>Heating Services</p>
    </div>
  </div>
</body>
</html>
```